Up to the Challenge - PPT Template with Splash Slide

We are looking for a PPT template that has 4 slides.
1. Splash slide (Creative, fun, no content, a visual representation of the theme)
2. Section header slide
3. Content Slide
4. Content Slide, another design option
The theme is 'UP to the Challenge'. The design should reflect this theme.
The colors should be in Purple (#864B99), Blue (#0A80C2), and Green (#52B054).

```html
<!DOCTYPE html>
<html lang="en">
<head>
<meta charset="utf-8">
<title>Up to the Challenge – Slide Template</title>
<link href="https://fonts.googleapis.com/css2?family=Poppins:wght@400;500;600&family=Montserrat:wght@400;500;600;700&display=swap" rel="stylesheet">
<style>
  :root {
    --purple: #864B99;
    --blue: #0A80C2;
    --blue-dark: #1A5E8C;
    --green: #52B054;
    --green-dark: #2F9238;
    --ink: #111111;
    --body: #333333;
    --muted: #666666;
    --canvas: #8A8A8A;
    --navy: #040B1C;
    --paper: #FFFFFF;
    --mist: #F1F1F1;
    --orange-light: #F6A53A;
    --orange-dark: #B5500F;
  }
  * { margin: 0; padding: 0; box-sizing: border-box; }
  html, body { width: 994px; height: 1200px; overflow: hidden; }
  body { background: var(--canvas); position: relative; font-family: "Montserrat", sans-serif; color: var(--body); }

  .slide { position: absolute; width: 441px; height: 248px; overflow: hidden; background: var(--paper); }
  .col-left { left: 41px; }
  .col-right { left: 512px; }
  .row-1 { top: 38px; }
  .row-2 { top: 325px; }
  .row-3 { top: 612px; }
  .row-4 { top: 898px; }

  .title { position: absolute; font-family: "Poppins", sans-serif; font-weight: 600; color: var(--ink); font-size: 13px; letter-spacing: 0.2px; line-height: 1; }
  .title-lg { font-size: 18px; }
  .rule { position: absolute; height: 2px; width: 29px; background: var(--purple); }

  /* splash */
  .splash-photo { position: absolute; left: 11px; top: 12px; width: 418px; height: 224px;
    background: linear-gradient(180deg, #CFE6FA 0%, #6FA4E8 40%, #2F5ED0 75%, #1A2F8A 100%); }
  .splash-jump { position: absolute; inset: 0;
    background: linear-gradient(180deg, var(--orange-light) 0%, #EE8A22 55%, var(--orange-dark) 100%); }

  /* intro dark */
  .intro-dark { background: var(--navy); }
  .intro-dark .title { color: #fff; left: 0; right: 0; text-align: center; top: 32px; }
  .intro-dark .rule { left: 206px; top: 57px; }
  .intro-chart { position: absolute; inset: 0;
    background: linear-gradient(165deg, rgba(4,11,28,0) 35%, rgba(20,140,150,0.4) 70%, rgba(30,200,200,0.65) 100%); }

  /* intro light */
  .intro-light .title { left: 21px; top: 21px; }
  .intro-light .rule { left: 22px; top: 45px; }
  .intro-darts { position: absolute; left: 225px; top: 0; right: 0; bottom: 0;
    background: radial-gradient(circle at 80% 60%, #D9D9D9 0%, #ECECEC 45%, rgba(255,255,255,0) 75%); }

  .soft-bg { background: linear-gradient(135deg, #F7F7F7 0%, #EDEDED 50%, #F6F6F6 100%); }

  /* about cards */
  .about-cards .title { left: 22px; top: 86px; }
  .about-cards .rule { left: 22px; top: 108px; }
  .about-cards .lead { position: absolute; left: 23px; top: 119px; font-size: 8.4px; color: var(--purple); font-weight: 500; }
  .about-cards .lead-text { position: absolute; left: 23px; top: 136px; width: 150px; font-size: 5.9px; line-height: 11px; color: var(--body); }
  .card { position: absolute; width: 106px; }
  .card-box { position: absolute; left: 313px; top: 51px; width: 105px; height: 72px; background: #fff; border-radius: 4px; box-shadow: 0 1px 5px rgba(0,0,0,0.12); }
  .card h3 { font-family: "Poppins", sans-serif; font-weight: 500; font-size: 9px; color: var(--ink); line-height: 1; }
  .card h4 { font-family: "Montserrat", sans-serif; font-weight: 700; font-size: 5.4px; color: var(--purple); margin-top: 6px; }
  .card p { font-size: 5.3px; line-height: 11px; margin-top: 3px; color: var(--body); }

  /* about text */
  .about-text .title { left: 22px; top: 17px; }
  .about-text .rule { left: 22px; top: 40px; }
  .about-text .column { position: absolute; top: 52px; width: 184px; font-size: 6.3px; line-height: 11.45px; text-align: justify; color: #222; }

  /* who we are */
  .who .title { left: 22px; top: 22px; }
  .who .rule { left: 22px; top: 45px; }
  .who .intro-text { position: absolute; left: 21px; top: 56px; width: 183px; font-size: 5.9px; line-height: 11.45px; color: #222; }
  .who .intro-text p + p { margin-top: 11.45px; }
  .pyramid, .chart { position: absolute; left: 0; top: 0; width: 441px; height: 248px; }

  /* graph */
  .graph .title { left: 0; right: 0; text-align: center; top: 24px; }
  .graph .rule { left: 208px; top: 46px; width: 23px; }
</style>
</head>
<body>

  <section class="slide col-left row-1 splash">
    <div class="splash-photo" role="img" aria-label="Photo: silhouette of one climber pulling another up onto a mountain peak above blue valleys"></div>
  </section>

  <section class="slide col-right row-1 splash">
    <div class="splash-jump" role="img" aria-label="Photo: silhouette of a person leaping across a gap between two cliffs at sunset, with the words I can't on the left cliff and Do it. on the right cliff"></div>
  </section>

  <section class="slide col-left row-2 intro-dark">
    <div class="intro-chart" role="img" aria-label="Illustration: glowing teal stock chart bars and grid rising into a dark background"></div>
    <h2 class="title title-lg">INTRODUCTION</h2>
    <div class="rule"></div>
  </section>

  <section class="slide col-right row-2 intro-light">
    <div class="intro-darts" role="img" aria-label="Faint photo: darts striking the bullseye of a dartboard"></div>
    <h2 class="title title-lg">INTRODUCTION</h2>
    <div class="rule"></div>
  </section>

  <section class="slide col-left row-3 soft-bg about-cards">
    <h2 class="title">ABOUT US</h2>
    <div class="rule"></div>
    <div class="lead">Lorem ipsum dolor</div>
    <p class="lead-text">Sed ut perspiciatis unde omnis iste natus error sit voluptatem accusantium doloremque laudantium, totam rem aperiam, eaque ipsa quae ab illo inventore veritatis et quasi architecto beatae vitae dicta sunt explicabo.</p>
    <div class="card-box"></div>
    <div class="card" style="left:204px;top:59px"><h3>Lorem ipsum</h3><h4>Excepteur sint</h4><p>Sed ut perspiciatis unde omnis iste veritatis et quasi architecto beatae vitae dicta sunt explicabo.</p></div>
    <div class="card" style="left:324px;top:59px"><h3>Lorem ipsum</h3><h4>Excepteur sint</h4><p>Sed ut perspiciatis unde omnis iste veritatis et quasi architecto beatae vitae dicta sunt explicabo.</p></div>
    <div class="card" style="left:204px;top:135px"><h3>Lorem ipsum</h3><h4>Excepteur sint</h4><p>Sed ut perspiciatis unde omnis iste veritatis et quasi architecto beatae vitae dicta sunt explicabo.</p></div>
    <div class="card" style="left:324px;top:135px"><h3>Lorem ipsum</h3><h4>Excepteur sint</h4><p>Sed ut perspiciatis unde omnis iste veritatis et quasi architecto beatae vitae dicta sunt explicabo.</p></div>
  </section>

  <section class="slide col-right row-3 soft-bg about-text">
    <h2 class="title">ABOUT US</h2>
    <div class="rule"></div>
    <p class="column" style="left:21px">Lorem ipsum dolor sit amet, consectetur adipiscing elit, sed do eiusmod tempor incididunt ut labore et dolore magna aliqua. Ut enim ad minim veniam, quis nostrud exercitation ullamco laboris nisi ut aliquip ex ea commodo consequat. Duis aute irure dolor in reprehenderit in voluptate velit esse cillum dolore eu fugiat nulla pariatur. Excepteur sint occaecat cupidatat non proident, sunt in culpa qui officia deserunt mollit anim id est laborum.Sed ut perspiciatis unde omnis iste natus error sit voluptatem accusantium doloremque laudantium, totam rem aperiam, eaque ipsa quae ab illo inventore veritatis et quasi architecto beatae vitae dicta sunt explicabo. Nemo enim ipsam voluptatem quia voluptas sit aspernatur aut odit aut fugit, sed quia consequuntur magni dolores eos qui ratione voluptatem sequi nesciunt.</p>
    <p class="column" style="left:232px">Lorem ipsum dolor sit amet, consectetur adipiscing elit, sed do eiusmod tempor incididunt ut labore et dolore magna aliqua. Ut enim ad minim veniam, quis nostrud exercitation ullamco laboris nisi ut aliquip ex ea commodo consequat. Duis aute irure dolor in reprehenderit in voluptate velit esse cillum dolore eu fugiat nulla pariatur. Excepteur sint occaecat cupidatat non proident, sunt in culpa qui officia deserunt mollit anim id est laborum.Sed ut perspiciatis unde omnis iste natus error sit voluptatem accusantium doloremque laudantium, totam rem aperiam, eaque ipsa quae ab illo inventore veritatis et quasi architecto beatae vitae dicta sunt explicabo. Nemo enim ipsam voluptatem quia voluptas sit aspernatur aut odit aut fugit, sed quia consequuntur magni dolores eos qui ratione voluptatem sequi nesciunt.</p>
  </section>

  <section class="slide col-left row-4 who">
    <h2 class="title">WHO WE ARE</h2>
    <div class="rule"></div>
    <div class="intro-text">
      <p>Sed ut perspiciatis unde omnis iste natus error sit voluptatem accusantium doloremque laudantium, totam rem aperiam, eaque ipsa quae ab illo inventore veritatis et quasi architecto beatae vitae dicta sunt explicabo. Nemo enim ipsam voluptatem quia voluptas sit aspernatur aut odit aut fugit, sed quia consequuntur magni dolores eos qui ratione voluptatem sequi nesciunt.</p>
      <p>Neque porro quisquam est, qui dolorem ipsum quia dolor sit amet, consectetur, adipisci velit, sed quia non numquam eius modi tempora incidunt ut labore et laboriosam, nisi ut aliquid ex ea commodi consequatur? Lorem ipsum dolor sit amet, consectetur exercitation ullamco laboris nisi ut aliquip ex ea commodo consequat.</p>
    </div>
    <svg class="pyramid" viewBox="0 0 771 433" font-family="Montserrat, sans-serif" fill="#fff" text-anchor="middle">
      <ellipse cx="562" cy="364" rx="177" ry="16" fill="var(--blue-dark)"/>
      <path d="M427 287 A135 10 0 0 1 697 287 L739 364 A177 16 0 0 1 385 364 Z" fill="var(--blue)"/>
      <text x="562" y="322" font-size="14">Supporter -</text>
      <text x="562" y="343" font-size="14" font-weight="500">up to CHF 10'000</text>
      <ellipse cx="562" cy="269" rx="136" ry="12" fill="var(--green-dark)"/>
      <path d="M472 197 A90 8 0 0 1 652 197 L698 269 A136 12 0 0 1 426 269 Z" fill="var(--green)"/>
      <text x="562" y="227" font-size="14">Sponsoring partner -</text>
      <text x="562" y="248" font-size="14" font-weight="500">From CHF 10'000</text>
      <ellipse cx="562" cy="184" rx="95" ry="10" fill="var(--blue-dark)"/>
      <path d="M515 114 A47 6 0 0 1 609 114 L657 184 A95 10 0 0 1 467 184 Z" fill="var(--blue)"/>
      <text x="562" y="139" font-size="14">Main partner -</text>
      <text x="562" y="160" font-size="14" font-weight="500">From CHF 25'000</text>
      <ellipse cx="562" cy="101" rx="55" ry="8" fill="var(--green-dark)"/>
      <path d="M536 29 A26 4 0 0 1 588 29 L617 101 A55 8 0 0 1 507 101 Z" fill="var(--green)"/>
      <text x="562" y="56" font-size="11">Strategic</text>
      <text x="562" y="70" font-size="11">partner -</text>
      <text x="562" y="83" font-size="9">From CHF 100,000</text>
    </svg>
  </section>

  <section class="slide col-right row-4 graph">
    <h2 class="title">GRAPH</h2>
    <div class="rule"></div>
    <svg class="chart" viewBox="0 0 771 433" font-family="Montserrat, sans-serif" fill="var(--muted)" font-size="12">
      <line x1="147" y1="109" x2="147" y2="309" stroke="#DDDDDD"/>
      <line x1="147" y1="309" x2="694" y2="309" stroke="#DDDDDD"/>
      <g text-anchor="end">
        <text x="133" y="124">25k</text>
        <text x="133" y="161">20k</text>
        <text x="133" y="197">15k</text>
        <text x="133" y="234">10k</text>
        <text x="133" y="270">5k</text>
      </g>
      <text transform="translate(88 198) rotate(-90)" text-anchor="middle">Reviews</text>
      <g fill="var(--blue)">
        <rect x="169" y="212" width="30" height="77"/>
        <rect x="214" y="167" width="30" height="122"/>
        <rect x="258" y="212" width="30" height="77"/>
        <rect x="301" y="136" width="30" height="153" fill="var(--green)"/>
        <rect x="344" y="229" width="30" height="60"/>
        <rect x="388" y="176" width="30" height="113"/>
        <rect x="432" y="191" width="30" height="98"/>
        <rect x="474" y="218" width="30" height="71"/>
        <rect x="518" y="167" width="30" height="122"/>
        <rect x="564" y="189" width="30" height="100"/>
        <rect x="610" y="167" width="30" height="122"/>
        <rect x="657" y="189" width="30" height="100"/>
      </g>
      <g text-anchor="middle">
        <text x="184" y="335">Jan</text><text x="229" y="335">Feb</text><text x="273" y="335">Mar</text>
        <text x="316" y="335">Apr</text><text x="359" y="335">May</text><text x="403" y="335">Jun</text>
        <text x="447" y="335">Jul</text><text x="489" y="335">Aug</text><text x="533" y="335">Sep</text>
        <text x="579" y="335">Oct</text><text x="625" y="335">Nov</text><text x="672" y="335">Dec</text>
        <text x="387" y="374" font-size="13">year</text>
      </g>
    </svg>
  </section>

</body>
</html>
```